Sentrova website

Clean website design for a security and website monitoring company so it needs to have a look that can be trusted and professional

These are the style of site we like
https://img.vorlaxo.net/564x/3c/71/e2/3c71e2a09b5f4d7c6e18a2b3f9d04c57.jpg
https://img.vorlaxo.net/564x/9d/42/7a/9d427a6e03bc51f8d2a7e4c90b16f38d.jpg
https://img.vorlaxo.net/564x/e7/0b/c4/e70bc4d2f8a1693e5b7d0c2af4e83b19.jpg

Different packages
- We will offer 3 different packages

Features are
- Monitoring site uptime

- Monitoring content changes on the site

- Check for hacking attempts

- Application firewall

- Monitoring SSL expiry

- Monitoring domain expiry

- Page load performance time

Industry/Entity Type

It Company

```html
<!DOCTYPE html>
<html lang="en">
<head>
<meta charset="utf-8">
<title>Sentrova — Security and Website Monitoring</title>
<link href="https://fonts.googleapis.com/css2?family=Poppins:wght@300;400;500;600;700&display=swap" rel="stylesheet">
<style>
:root{
  --navy:#1e2943;
  --navy-deep:#151d31;
  --crimson:#c8495c;
  --pink:#f1899a;
  --pink-soft:#f6b3be;
  --ink:#222a3a;
  --body:#6b6f7a;
  --grey-band:#7d7c7a;
  --light:#f5f6f8;
  --white:#ffffff;
}
*{box-sizing:border-box;margin:0;padding:0}
html,body{width:1200px;height:3879px;overflow:hidden}
body{font-family:"Poppins",sans-serif;color:var(--ink);background:var(--white);position:relative}
.abs{position:absolute}
p{line-height:1.75}

/* header + hero */
.hero{left:0;top:0;width:1200px;height:647px;background:linear-gradient(120deg,#2a3654 0%,#1e2943 55%,#18213a 100%)}
.hero-cut{left:0;top:0;width:1200px;height:647px}
.brand{display:flex;align-items:center;gap:12px;font-weight:600;font-size:30px;color:var(--white);white-space:nowrap}
.brand-dot{width:40px;height:40px;border-radius:50%;background:var(--crimson);flex:none}
.nav{left:564px;top:46px;display:flex;gap:34px;font-size:17px;color:var(--white)}
.login{left:1021px;top:44px;width:78px;height:38px;border:2px solid var(--white);border-radius:4px;color:var(--white);font-size:14px;font-weight:600;display:flex;align-items:center;justify-content:center}
.hero-title{left:98px;top:200px;font-size:48px;font-weight:600;line-height:1.2;color:var(--white)}
.hero-text{left:98px;top:328px;width:470px;font-size:14px;color:#d9dde6;line-height:1.65}
.btn-light{left:98px;top:421px;width:166px;height:36px;border-radius:18px;background:var(--white);color:var(--ink);font-size:15px;display:flex;align-items:center;justify-content:center}
.dots{left:98px;top:481px;display:flex;gap:7px}
.dots span{width:14px;height:14px;border-radius:50%;border:2px solid var(--white)}
.dots span:first-child{background:var(--white)}
.screen{border-radius:10px;background:linear-gradient(160deg,#d7dbe2 0%,#5d6a7f 45%,#2c3447 100%)}

/* welcome */
.section-title{width:1200px;left:0;text-align:center;font-weight:600;color:var(--ink)}
.welcome-title{top:736px;font-size:36px}
.welcome-text{left:134px;top:796px;width:932px;text-align:center;font-size:13px;color:var(--body)}
.feature{width:330px;display:flex;gap:22px}
.feature svg{flex:none}
.feature h3{font-size:17px;font-weight:500;line-height:1.35;color:var(--ink);margin-top:6px}
.feature p{font-size:13px;color:var(--body);margin-top:8px;line-height:1.65}

/* split sections */
.split{left:0;width:1200px;height:479px;background:var(--light)}
.split-title{font-size:33px;font-weight:500;color:var(--ink);white-space:nowrap}
.split-text{width:470px;font-size:12.5px;color:var(--body);line-height:1.85}
.btn-red{width:108px;height:34px;border-radius:17px;background:var(--crimson);color:var(--white);font-size:14px;font-weight:500;display:flex;align-items:center;justify-content:center}

/* packages */
.packages{left:0;top:1875px;width:1200px;height:711px;background:linear-gradient(135deg,#28344f 0%,#1e2943 50%,#1a2338 100%)}
.pk-title{top:1952px;font-size:36px;color:var(--white)}
.pk-text{left:330px;top:2004px;width:540px;text-align:center;font-size:14px;color:#d9dde6;line-height:1.6}
.card{background:var(--white);box-shadow:0 6px 24px rgba(0,0,0,.18);text-align:center}
.card h3{font-size:26px;font-weight:600;color:var(--ink);height:70px;display:flex;align-items:center;justify-content:center}
.price{height:83px;background:var(--grey-band);color:var(--white);display:flex;align-items:center;justify-content:center;font-size:46px;font-weight:500}
.price sup{font-size:20px;align-self:flex-start;margin-top:14px}
.price small{font-size:20px;font-weight:400;margin-top:16px}
.card ul{list-style:none;margin-top:18px}
.card li{font-size:12.5px;color:var(--body);padding:8px 0;border-bottom:1px solid #eceef1;margin:0 16px;white-space:nowrap}
.card li:last-child{border-bottom:0}
.btn-grey{display:inline-flex;width:106px;height:32px;align-items:center;justify-content:center;background:var(--grey-band);color:var(--white);font-size:12px;font-weight:600;letter-spacing:.5px;margin-top:24px}
.card.featured .price{background:var(--crimson)}
.card.featured .btn-grey{background:var(--crimson)}

/* testimonials */
.cl-title{top:2640px;font-size:36px}
.cl-rule{left:570px;top:2706px;width:60px;height:3px;background:var(--crimson)}
.quote{width:320px}
.quote p{font-size:12.5px;font-style:italic;color:var(--body);line-height:1.7;position:relative;padding-left:14px}
.quote p::before{content:"\201C";position:absolute;left:0;top:-8px;font-size:28px;color:var(--ink);font-style:normal}
.person{display:flex;align-items:center;gap:22px;margin-top:30px}
.avatar{width:72px;height:72px;border-radius:50%;background:linear-gradient(150deg,#c9b9a8,#6d6a6f)}
.person span{display:block;font-size:14px;color:var(--ink);line-height:1.45}

/* footer */
.footer{left:0;top:3504px;width:1200px;height:375px;background:var(--navy-deep)}
.ft-logo{left:118px;top:3556px;width:200px;display:flex;flex-direction:column;align-items:center;gap:12px;color:var(--white);font-size:24px;font-weight:500}
.ft-logo .brand-dot{width:42px;height:42px}
.social{display:flex;gap:8px;margin-top:6px}
.social span{width:28px;height:28px;border-radius:50%;border:2px solid var(--white)}
.ft-head{font-size:17px;font-weight:600;color:var(--white);letter-spacing:.3px}
.ft-list{list-style:none;font-size:14px;color:#d5d9e2}
.ft-contact li{display:flex;gap:16px;align-items:flex-start;margin-bottom:14px;line-height:1.5}
.ft-links li{margin-bottom:4px}
.ft-text{width:300px;font-size:12px;color:#c9ced8;line-height:1.6}
.field{width:285px;height:42px;background:var(--white);font-size:12px;color:#8b8f98;padding-left:14px;display:flex;align-items:center}
.btn-sub{width:100px;height:38px;background:var(--crimson);color:var(--white);font-size:12px;font-weight:600;display:flex;align-items:center;justify-content:center}
.ft-rule{left:0;top:3800px;width:1200px;height:1px;background:#2c3650}
.copy{left:0;top:3824px;width:1200px;text-align:center;font-size:12px;color:#c9ced8}
</style>
</head>
<body>

<!-- Hero -->
<div class="abs hero" role="img" aria-label="Dim office photograph with a person at a desk behind a navy overlay"></div>
<svg class="abs hero-cut" viewBox="0 0 1200 647" aria-hidden="true"><polygon points="0,647 1200,545 1200,647" fill="#ffffff"/></svg>

<div class="abs brand" style="left:98px;top:44px"><span class="brand-dot"></span>sentrova.com</div>
<nav class="abs nav"><span>Home</span><span>About</span><span>Services</span><span>Blog</span><span>Contact Us</span></nav>
<div class="abs login">LOGIN</div>

<h1 class="abs hero-title">Security And<br>Website Monitoring</h1>
<p class="abs hero-text">Sed ut perspiciatis unde omnis iste natus error sit voluptatem accusantium doloremque laudantium, totam rem aperiam, eaque ipsa quae ab illo inventore veritatis et quasi</p>
<div class="abs btn-light">Learn More</div>
<div class="abs dots"><span></span><span></span><span></span></div>

<div class="abs screen" style="left:693px;top:354px;width:406px;height:331px" role="img" aria-label="Desktop monitor showing a video of a man working at a computer"></div>

<!-- Welcome -->
<h2 class="abs section-title welcome-title">WELCOME TO SENTROVA</h2>
<p class="abs welcome-text">Sed ut perspiciatis unde omnis iste natus error sit voluptatem accusantium doloremque laudantium, totam rem aperiam, eaque ipsa quae ab illo inventore veritatis et quasi architecto beatae vitae dicta sunt explicabo. Nemo enim ipsam voluptatem quia voluptas sit aspernatur aut odit aut fugit, sed quia consequuntur magni dolores eos qui ratione voluptatem sequi nesciunt. Neque porro quisquam doloremque</p>

<svg width="0" height="0" style="position:absolute">
  <defs>
    <symbol id="shield" viewBox="0 0 84 96">
      <path d="M42 4 L78 16 V46 C78 70 62 84 42 92 C22 84 6 70 6 46 V16 Z" fill="none" stroke="#c8495c" stroke-width="4"/>
      <path d="M42 12 L70 22 V46 C70 65 58 76 42 83 C26 76 14 65 14 46 V22 Z" fill="none" stroke="#9fc1a8" stroke-width="2.5"/>
    </symbol>
  </defs>
</svg>

<div class="abs feature" style="left:98px;top:944px">
  <svg width="84" height="96" viewBox="0 0 84 96"><use href="#shield"/><rect x="27" y="34" width="30" height="22" rx="2" fill="none" stroke="#c8495c" stroke-width="2.5"/><path d="M36 62 H48 M42 56 V62" stroke="#c8495c" stroke-width="2.5"/><circle cx="42" cy="45" r="5" fill="none" stroke="#c8495c" stroke-width="2"/></svg>
  <div><h3>Monitoring site<br>uptime</h3><p>Sed ut perspiciatis unde omnis iste natus error sit voluptatem accusantium doloremque ntium, totam rem aperiam</p></div>
</div>
<div class="abs feature" style="left:445px;top:944px">
  <svg width="84" height="96" viewBox="0 0 84 96"><use href="#shield"/><rect x="29" y="30" width="26" height="32" rx="2" fill="none" stroke="#c8495c" stroke-width="2.5"/><path d="M34 39 H50 M34 46 H50 M34 53 H45" stroke="#c8495c" stroke-width="2"/></svg>
  <div><h3>Monitoring content<br>changes on the site</h3><p>Sed ut perspiciatis unde omnis iste natus error sit voluptatem accusantium doloremque ntium, totam rem aperiam</p></div>
</div>
<div class="abs feature" style="left:794px;top:944px">
  <svg width="84" height="96" viewBox="0 0 84 96"><use href="#shield"/><circle cx="42" cy="46" r="11" fill="none" stroke="#c8495c" stroke-width="2.5"/><circle cx="42" cy="46" r="4" fill="#c8495c"/><path d="M42 30 V35 M42 57 V62 M26 46 H31 M53 46 H58" stroke="#c8495c" stroke-width="3"/></svg>
  <div><h3>Check for hacking<br>attempts</h3><p>Sed ut perspiciatis unde omnis iste natus error sit voluptatem accusantium doloremque ntium, totam rem aperiam</p></div>
</div>
<div class="abs feature" style="left:98px;top:1146px">
  <svg width="84" height="96" viewBox="0 0 84 96"><use href="#shield"/><rect x="26" y="34" width="32" height="24" fill="none" stroke="#c8495c" stroke-width="2.5"/><path d="M26 42 H58 M26 50 H58 M36 34 V42 M48 42 V50 M36 50 V58" stroke="#c8495c" stroke-width="2"/></svg>
  <div><h3>Application<br>firewall</h3><p>Sed ut perspiciatis unde omnis iste natus error sit voluptatem accusantium doloremque ntium, totam rem aperiam</p></div>
</div>
<div class="abs feature" style="left:445px;top:1146px">
  <svg width="84" height="96" viewBox="0 0 84 96"><use href="#shield"/><text x="42" y="54" text-anchor="middle" font-family="Poppins,sans-serif" font-size="17" font-weight="700" fill="#222a3a">SSL</text></svg>
  <div><h3>Monitoring SSL<br>expiry</h3><p>Sed ut perspiciatis unde omnis iste natus error sit voluptatem accusantium doloremque ntium, totam rem aperiam</p></div>
</div>
<div class="abs feature" style="left:794px;top:1146px">
  <svg width="84" height="96" viewBox="0 0 84 96"><use href="#shield"/><circle cx="42" cy="46" r="14" fill="none" stroke="#c8495c" stroke-width="2.5"/><ellipse cx="42" cy="46" rx="6" ry="14" fill="none" stroke="#c8495c" stroke-width="2"/><path d="M28 46 H56" stroke="#c8495c" stroke-width="2"/></svg>
  <div><h3>Monitoring domain<br>expiry</h3><p>Sed ut perspiciatis unde omnis iste natus error sit voluptatem accusantium doloremque ntium, totam rem aperiam</p></div>
</div>

<!-- Website monitoring -->
<div class="abs split" style="top:1396px"></div>
<svg class="abs" style="left:0;top:1396px" width="1200" height="479" viewBox="0 0 1200 479" aria-hidden="true">
  <polygon points="0,0 640,300 470,479 0,479" fill="#c8495c"/>
  <polygon points="560,479 760,370 960,479" fill="#f6b3be"/>
  <polygon points="760,479 1200,230 1200,479" fill="#f1899a"/>
</svg>
<div class="abs screen" style="left:98px;top:1495px;width:517px;height:295px" role="img" aria-label="Laptop, tablet and phone on a wooden desk showing a responsive website"></div>
<h2 class="abs split-title" style="left:657px;top:1468px">Website Monitoring</h2>
<p class="abs split-text" style="left:660px;top:1530px">Sed ut perspiciatis unde omnis iste natus error sit voluptatem accusantium doloremque laudantium, totam rem aperiam, eaque ipsa quae ab illo inventore veritatis et quasi architecto beatae vitae dicta sunt explicabo. Nemo enim ipsam voluptatem quia voluptas sit aspernatur</p>
<div class="abs btn-red" style="left:665px;top:1658px">Read More</div>

<!-- Packages -->
<div class="abs packages" role="img" aria-label="Office workspace photograph behind a dark navy overlay"></div>
<h2 class="abs section-title pk-title">OUR PACKAGES</h2>
<p class="abs pk-text">Nemo enim ipsam voluptatem quia voluptas sit aspernatur aut odit aut fugit, sed quia consequuntur magni dolores eos qui ratione voluptatem</p>

<div class="abs card" style="left:150px;top:2133px;width:284px;height:401px">
  <h3>Standard</h3>
  <div class="price"><sup>$</sup>20<small>/user/m</small></div>
  <ul><li>Mauris at lacus tempus arcu</li><li>Donec quis odio nec sem malesuada</li><li>Quisque laoreet diam quis</li><li>Vestibulum maximus</li></ul>
  <span class="btn-grey">GET STARTED</span>
</div>
<div class="abs card" style="left:766px;top:2133px;width:284px;height:401px">
  <h3>Professional</h3>
  <div class="price"><sup>$</sup>60<small>/user/m</small></div>
  <ul><li>Mauris at lacus tempus arcu</li><li>Donec quis odio nec sem malesuada</li><li>Quisque laoreet diam quis</li><li>Vestibulum maximus</li></ul>
  <span class="btn-grey">GET STARTED</span>
</div>
<div class="abs card featured" style="left:434px;top:2108px;width:332px;height:452px">
  <h3>Premium</h3>
  <div class="price" style="height:94px"><sup>$</sup>40<small>/user/m</small></div>
  <ul><li>Mauris at lacus tempus arcu</li><li>Donec quis odio nec sem malesuada</li><li>Quisque laoreet diam quis</li><li>Vestibulum maximus</li></ul>
  <span class="btn-grey">GET STARTED</span>
</div>

<!-- Testimonials -->
<h2 class="abs section-title cl-title">WHAT DO OUR CLIENTS SAY?</h2>
<div class="abs cl-rule"></div>

<div class="abs quote" style="left:98px;top:2758px">
  <p>Lorem ipsum dolor sit amet, consectetur adipisicing elit, sed do eiusmod tempor incididunt ut labore et dolore magna aliqua Ut enim ad minim veniam, consequuntur.</p>
  <div class="person"><div class="avatar" role="img" aria-label="Portrait photo of the client"></div><div><span>Dana Merrow</span><span>sentrova</span></div></div>
</div>
<div class="abs quote" style="left:450px;top:2758px">
  <p>Lorem ipsum dolor sit amet, consectetur adipisicing elit, sed do eiusmod tempor incididunt ut labore et dolore magna aliqua Ut enim ad minim veniam, consequuntur.</p>
  <div class="person"><div class="avatar" role="img" aria-label="Portrait photo of the client"></div><div><span>Dana Merrow</span><span>sentrova</span></div></div>
</div>
<div class="abs quote" style="left:804px;top:2758px">
  <p>Lorem ipsum dolor sit amet, consectetur adipisicing elit, sed do eiusmod tempor incididunt ut labore et dolore magna aliqua Ut enim ad minim veniam, consequuntur.</p>
  <div class="person"><div class="avatar" role="img" aria-label="Portrait photo of the client"></div><div><span>Dana Merrow</span><span>sentrova</span></div></div>
</div>

<!-- Security monitoring -->
<div class="abs split" style="top:3026px"></div>
<svg class="abs" style="left:0;top:3026px" width="1200" height="478" viewBox="0 0 1200 478" aria-hidden="true">
  <polygon points="0,220 500,478 0,478" fill="#f1899a"/>
  <polygon points="380,478 560,380 740,478" fill="#f6b3be"/>
  <polygon points="640,478 1200,40 1200,478" fill="#c8495c"/>
</svg>
<h2 class="abs split-title" style="left:202px;top:3080px">Security Monitoring</h2>
<p class="abs split-text" style="left:202px;top:3142px">Sed ut perspiciatis unde omnis iste natus error sit voluptatem accusantium doloremque laudantium, totam rem aperiam, eaque ipsa quae ab illo inventore veritatis et quasi architecto beatae vitae dicta sunt explicabo. Nemo enim ipsam voluptatem quia voluptas sit aspernatur</p>
<div class="abs btn-red" style="left:202px;top:3270px">Read More</div>
<div class="abs screen" style="left:693px;top:3103px;width:406px;height:323px" role="img" aria-label="Desktop monitor showing a man working at a multi-screen security station"></div>

<!-- Footer -->
<footer class="abs footer"></footer>
<div class="abs ft-logo">
  <span class="brand-dot"></span>
  <span>sentrova.com</span>
  <div class="social"><span></span><span></span><span></span><span></span></div>
</div>

<h4 class="abs ft-head" style="left:328px;top:3548px">CONTACT US</h4>
<ul class="abs ft-list ft-contact" style="left:328px;top:3594px;width:250px">
  <li><svg width="16" height="20" viewBox="0 0 16 20"><path d="M8 1 C4 1 1 4 1 8 C1 13 8 19 8 19 C8 19 15 13 15 8 C15 4 12 1 8 1 Z" fill="none" stroke="#fff" stroke-width="1.8"/><circle cx="8" cy="8" r="2.5" fill="#fff"/></svg><span>Sentrova 48 Harbour Lane<br>Singapore 100482</span></li>
  <li><svg width="16" height="18" viewBox="0 0 16 18"><path d="M3 1 L6 1 L7 5 L5 7 C6 10 8 12 11 13 L13 11 L16 12 V15 C16 16 15 17 14 17 C7 16 1 10 1 3 C1 2 2 1 3 1 Z" fill="#fff"/></svg><span>Phone : 900 4127 3310</span></li>
  <li><svg width="18" height="14" viewBox="0 0 18 14"><rect x="1" y="1" width="16" height="12" fill="none" stroke="#fff" stroke-width="1.8"/><path d="M1 1 L9 8 L17 1" fill="none" stroke="#fff" stroke-width="1.8"/></svg><span>info@sentrova.com</span></li>
</ul>

<h4 class="abs ft-head" style="left:605px;top:3548px">SIGN UP TO RECEIVE EMAIL</h4>
<p class="abs ft-text" style="left:605px;top:3590px">Excepteur sint occaecat cupidatat non proident, sunt in culpa qui Nemo enim ipsam voluptatem</p>
<div class="abs field" style="left:605px;top:3655px">Enter Name</div>
<div class="abs btn-sub" style="left:605px;top:3713px">SUBSCRIBE</div>

<h4 class="abs ft-head" style="left:985px;top:3548px">QUICK LINKS</h4>
<ul class="abs ft-list ft-links" style="left:985px;top:3590px">
  <li>Home</li><li>About Us</li><li>Features</li><li>Pricing</li><li>Log in</li><li>Contact Us</li>
</ul>

<div class="abs ft-rule"></div>
<p class="abs copy">Copyright © Sentrova 2018. All rights reserved.</p>

</body>
</html>
```